Brisley Global Sourcing - we are Asian sourcing agents

We are sourcing agents based in the USA and we act as sourcing agents for clients in throughout the world. We focus primarily on custom sewn goods. So basically companies who do not have the in-house expertise to do it themselves, come to us and have us find suitable factories in Asia to do the production. We are middlemen. We find the factories...quote the project...manage the quality control and then deliver the goods directly to our customer's door. We pride ourselves in making the communication very easy and precise.

Current page is www.brisleysourcing.com

I am not happy w/ the overall look. The spacing...the photos, the fonts...the design elements...the pictures. I want a cool, crisp design that conveys professionalism and clearly depicts/explains what we do.

Coding

Coded - Design and coding required

Number of Pages Required

5+ page

Requirements
Must have
• use my logo....I like it...it was designed by someone on this website.
Nice to have
• a video/animation of the entire process would be wonderful. Showing initial contact with our office in the USA...then to my correspondence with my offices in Taiwan and in Hong Kong...and then back and fort w/ the customer.....and then between my people in Hong Kong/Taiwan with the local factories......and then a quote is generated and sent to my client......to samples being made and sent for approval.....to a PO being generated......to final samples being sent.....to the order being shipped and delivered to the clients warehouse. I was thinking of an animation showing arrows and text showing the back and forth communication and explaining how the process flows.

```html
<!DOCTYPE html>
<html lang="en">
<head>
<meta charset="utf-8">
<title>Brisley Global Sourcing</title>
<link href="https://fonts.googleapis.com/css2?family=Arimo:wght@400;700&display=swap" rel="stylesheet">
<style>
:root{
  --navy:#0e1e5e;
  --navy-deep:#0a1648;
  --navy-bar:#081236;
  --hero:#2c3f86;
  --hero-edge:#152a6e;
  --green:#7a9a10;
  --text:#555;
  --muted:#8a8a8a;
  --rule:#dcdcdc;
  --panel:#efefef;
  --white:#fff;
}
*{margin:0;padding:0;box-sizing:border-box}
html,body{width:1046px;height:1200px;overflow:hidden}
body{position:relative;background:var(--white);font-family:"Arimo",Arial,sans-serif;color:var(--text)}
.abs{position:absolute}

/* header */
.contact-strip{top:4px;left:514px;font-size:7.5px;color:#444;display:flex;align-items:center;gap:6px;height:12px}
.contact-strip svg{width:9px;height:9px;fill:#333}
.contact-strip .gap{width:14px}
.brand{top:36px;left:226px;font-size:21px;font-weight:700;color:var(--navy);letter-spacing:-.2px;line-height:1}
.nav{top:36px;left:596px;display:flex;gap:0;font-size:7.8px;font-weight:700;color:#666;letter-spacing:.2px}
.nav a{text-decoration:none;color:inherit;margin-right:24px}
.nav a.current{color:var(--green)}
.nav-mark{top:52px;left:596px;width:24px;height:8px}

/* hero */
.hero{top:79px;left:0;width:1046px;height:286px;background:var(--hero-edge)}
.hero-photo{top:79px;left:24px;width:1008px;height:286px;background:linear-gradient(120deg,#3b4f95 0%,#2c3f86 45%,#3a4c8f 70%,#24377c 100%)}
.hero-title{top:172px;left:0;width:1046px;text-align:center;color:var(--white);font-size:24px;font-weight:700}
.hero-sub{top:201px;left:0;width:1046px;text-align:center;color:var(--white);font-size:13px}
.hero-btn{top:235px;left:467px;width:129px;height:30px;border:1.5px solid var(--white);color:var(--white);font-size:11px;font-weight:700;display:flex;align-items:center;justify-content:center}
.hero-arrow{top:220px;width:14px;height:24px}
.dots{top:332px;left:514px;display:flex;gap:3px}
.dots span{width:6px;height:6px;border-radius:50%;background:var(--white)}
.dots span.on{background:var(--green)}

/* feature columns */
.card-img{top:401px;height:95px;border:2px solid var(--green);border-radius:3px}
.badge{top:476px;width:34px;height:34px;border-radius:50%;background:var(--white);border:2px solid var(--green);display:flex;align-items:center;justify-content:center;color:#777;font-size:18px;font-weight:700}
.col-head{top:522px;font-size:13.5px;color:#555;text-align:center;letter-spacing:.2px}
.col-rule{top:541px;height:1px;background:var(--rule)}
.link-list{top:553px;list-style:none;font-size:8px;color:var(--muted);letter-spacing:.2px}
.link-list li{height:18.4px;display:flex;align-items:center}
.link-list li::before{content:"›";color:#bbb;margin-right:12px;font-size:9px}

.cta{top:401px;left:650px;width:189px;height:280px;background:var(--green);border-radius:3px;overflow:hidden}
.cta-photo{width:100%;height:95px;background:linear-gradient(180deg,#8a6a5a 0%,#6e4f44 55%,#3a3432 100%)}
.cta-head{position:absolute;top:114px;left:18px;width:160px;font-size:14.5px;color:var(--white);line-height:1.27}
.cta-text{position:absolute;top:186px;left:20px;width:160px;font-size:7.6px;color:var(--white);line-height:1.6}
.cta-btn{position:absolute;top:227px;left:20px;width:147px;height:27px;background:var(--white);color:var(--green);font-size:8px;font-weight:700;letter-spacing:.4px;display:flex;align-items:center;justify-content:center}

/* about band */
.about-band{top:732px;left:0;width:1046px;height:193px;background:var(--panel)}
.about-head{top:775px;left:0;width:1046px;text-align:center;font-size:17px;font-weight:700;color:#666}
.about-copy{top:807px;left:305px;width:456px;text-align:center;font-size:7.6px;line-height:1.62;color:#777}
.about-btn{top:860px;left:485px;width:95px;height:27px;border:1.5px solid #555;color:#555;font-size:8px;font-weight:700;letter-spacing:.8px;display:flex;align-items:center;justify-content:center}

/* footer */
.footer{top:925px;left:0;width:1046px;height:245px;background:var(--navy)}
.footer-brand{top:977px;left:226px;font-size:15.5px;font-weight:700;color:var(--white);line-height:1.1;width:130px}
.footer-info{top:976px;left:419px;color:var(--white);font-size:7.4px;line-height:1.65}
.footer-info h3{font-size:10px;font-weight:400;margin-bottom:3px}
.footer-info .space{height:10px}
.footer-links{top:976px;left:629px;color:var(--white)}
.footer-links h3{font-size:10px;font-weight:400;letter-spacing:.3px;margin-bottom:17px}
.footer-links ul{list-style:none;font-size:7.6px}
.footer-links li{height:18.4px}
.legal{top:1170px;left:0;width:1046px;height:30px;background:var(--navy-bar);color:#7c86ad;font-size:7px;display:flex;align-items:center;justify-content:center}
</style>
</head>
<body>

<header>
  <div class="abs contact-strip">
    <svg viewBox="0 0 10 10"><path d="M5 0a3.4 3.4 0 0 0-3.4 3.4C1.6 6 5 10 5 10s3.4-4 3.4-6.6A3.4 3.4 0 0 0 5 0zm0 4.8a1.4 1.4 0 1 1 0-2.8 1.4 1.4 0 0 1 0 2.8z"/></svg>
    <span>48 Harbor Lane Suite B-2 Dover, NH 03820</span>
    <span class="gap"></span>
    <svg viewBox="0 0 10 10"><path d="M1 3.5C2.5 1 7.5 1 9 3.5L7.6 5 6.4 4V3H3.6v1L2.4 5z M2.5 6h5l1 3h-7z"/></svg>
    <span>(603)-555-0142 &nbsp;|</span>
    <span class="gap"></span>
    <svg viewBox="0 0 10 10"><path d="M2.5 0h5v3h-5z M0 3.5h10V8H8V6H2v2H0z M2.5 6.8h5V10h-5z"/></svg>
    <span>(603)-555-0178</span>
  </div>
  <div class="abs brand">Brisley Global Sourcing</div>
  <nav class="abs nav">
    <a class="current" href="#">HOME</a>
    <a href="#">ABOUT US</a>
    <a href="#">PRODUCT CATEGORIES</a>
    <a href="#">CONTACT</a>
  </nav>
  <svg class="abs nav-mark" viewBox="0 0 24 8"><line x1="0" y1="4" x2="24" y2="4" stroke="#7a9a10" stroke-width="1"/><circle cx="12" cy="4" r="3" fill="none" stroke="#555" stroke-width="1"/></svg>
</header>

<section>
  <div class="abs hero"></div>
  <div class="abs hero-photo" role="img" aria-label="Close-up of a sewing machine stitching fabric, tinted blue"></div>
  <svg class="abs hero-arrow" style="left:110px" viewBox="0 0 14 24"><polyline points="12,2 2,12 12,22" fill="none" stroke="#fff" stroke-width="1.4"/></svg>
  <svg class="abs hero-arrow" style="left:922px" viewBox="0 0 14 24"><polyline points="2,2 12,12 2,22" fill="none" stroke="#fff" stroke-width="1.4"/></svg>
  <h1 class="abs hero-title">Asian Outsourcing Made Easy!</h1>
  <p class="abs hero-sub">Custom Sewn Goods Made to Your Specifications</p>
  <div class="abs hero-btn">Request a Quote</div>
  <div class="abs dots"><span class="on"></span><span></span><span></span><span></span></div>
</section>

<section>
  <div class="abs card-img" style="left:226px;width:190px;background:linear-gradient(135deg,#e8e8e8 0%,#cfd2d4 40%,#9bc22a 55%,#c9cccf 80%)" role="img" aria-label="Keyboard with a green Solution key"></div>
  <div class="abs badge" style="left:304px">
    <svg width="16" height="18" viewBox="0 0 16 18"><path d="M8 1.5a5 5 0 0 0-3 9v2.5h6v-2.5a5 5 0 0 0-3-9z M5.5 14.5h5 M6 16.5h4" fill="none" stroke="#777" stroke-width="1.2"/></svg>
  </div>
  <h2 class="abs col-head" style="left:226px;width:190px">SOURCING SOLUTIONS</h2>
  <div class="abs col-rule" style="left:226px;width:190px"></div>
  <ul class="abs link-list" style="left:226px">
    <li>BAGS</li><li>CASES</li><li>COVERS</li><li>GLOVES</li><li>MEDICAL</li><li>SEWN GOODS</li><li>SPORTING GOODS</li>
  </ul>

  <div class="abs card-img" style="left:437px;width:189px;background:radial-gradient(circle at 60% 35%,#c8d4f0 0%,#5d72a8 30%,#1d2c5c 75%)" role="img" aria-label="Rows of light bulbs with one glowing"></div>
  <div class="abs badge" style="left:514px">?</div>
  <h2 class="abs col-head" style="left:437px;width:189px">NEED TO KNOW</h2>
  <div class="abs col-rule" style="left:437px;width:189px"></div>
  <ul class="abs link-list" style="left:437px">
    <li>CONTRACT SEWING IN CHINA</li><li>WHAT IS THE PROCESS?</li><li>WHAT THE MINIMUM ORDER?</li><li>CONTRACT OUTSOURCING FAQ</li><li>OUTSOURCING CASE STUDY</li><li>CUSTOM INDUSTRIAL SEWING IN CHINA</li>
  </ul>

  <div class="abs cta">
    <div class="cta-photo" role="img" aria-label="Company founder standing in front of a historic building in China"></div>
    <h2 class="cta-head">Outsource Your Sewing Needs to Trusted Contractors in China</h2>
    <p class="cta-text">Please contact us for immediate consultation regarding your outsourcing project.</p>
    <div class="cta-btn">REQUEST A QUOTE</div>
  </div>
</section>

<section>
  <div class="abs about-band"></div>
  <h2 class="abs about-head">Sourcing custom goods in China</h2>
  <p class="abs about-copy">We outsource sewing services direct from China. Our long-established and extensive network of offshore factory-partners provides our clients with access to a wide variety of contract sewing expertise from Chinese manufacturers. Clients only need to communicate with our US agents, but will have the benefits of the cost savings &amp; quality workmanship from offshore outsourcing from Asia.</p>
  <div class="abs about-btn">ABOUT US</div>
</section>

<footer>
  <div class="abs footer"></div>
  <div class="abs footer-brand">Brisley Global Sourcing</div>
  <div class="abs footer-info">
    <h3>Brisley Global Sourcing, LLC</h3>
    <p>48 Harbor Lane<br>Suite B-2<br>Dover, NH 03820</p>
    <div class="space"></div>
    <p>Online: Inquiry Form<br>Tel: 603-555-0142<br>Fax: 603-555-0178<br>Email: ray@brisleysourcing.com</p>
  </div>
  <div class="abs footer-links">
    <h3>SOURCING SOLUTIONS</h3>
    <ul><li>Bags</li><li>Cases</li><li>Covers</li><li>Gloves</li><li>Medical</li><li>Sewn Goods</li><li>Sporting Goods</li></ul>
  </div>
  <div class="abs legal">© 2015, Brisley Global Sourcing, LLC. | USA - Hong Kong - Taipei</div>
</footer>

</body>
</html>
```